Tidal Quill is a premium Spa and Salon only professional tanning brand.

We need a email template/newsletter that we can send to our client base any time we would like to share information with them.
Whether this is launching our Christmas gift, or sharing up and coming training dates it will be another avenue for us to stay in touch with our clients.
We like to think ourselves as the 'Verrington handbag' in the tanning world, Tidal Quill is a brand that is desirable and exclusive and has people hooked once they trial the brand and are blown away by the results.
www.tidal-quill-example.com

```html
<!DOCTYPE html>
<html lang="en">
<head>
<meta charset="utf-8">
<title>Tidal Quill Newsletter</title>
<link rel="stylesheet" href="https://fonts.googleapis.com/css2?family=Lato:ital,wght@0,400;0,700;0,900;1,400;1,700;1,900&display=swap">
<style>
:root{
  --backdrop:#2c3744;
  --accent-orange:#e8893a;
  --frame-tan:#d4ae85;
  --panel:#ececec;
  --card:#ffffff;
  --brown-dark:#7a2a12;
  --brown:#9a4a22;
  --brown-soft:#b86a3e;
  --text-muted:#a8643c;
  --grey-caption:#9a9a9a;
  --white:#ffffff;
}
*{margin:0;padding:0;box-sizing:border-box}
html,body{width:761px;height:1200px;overflow:hidden;background:var(--backdrop)}
body{position:relative;font-family:'Lato',sans-serif}
.abs{position:absolute}
.proposal-label{left:21px;top:12px;color:var(--accent-orange);font-style:italic;font-size:14px;letter-spacing:.5px}
.proposal-title{left:21px;top:32px;color:var(--accent-orange);font-style:italic;font-weight:900;font-size:22.5px}
.frame{left:21px;top:73px;width:719px;height:1113px;background:var(--frame-tan);overflow:hidden}
.panel{left:28px;top:27px;width:667px;height:1040px;background:var(--panel)}
.swoosh-top{left:-68px;top:-87px;width:280px;height:240px;border-radius:50%;background:var(--white)}
.swoosh-bottom{right:-40px;bottom:-50px;width:150px;height:130px;border-radius:50%;background:var(--white)}
.brand-name{left:-14px;top:42px;font-weight:900;font-size:28px;color:var(--brown-soft);display:flex;align-items:center;gap:8px}
.brand-name i{display:block;width:18px;height:18px;border-radius:50%;background:var(--brown-soft)}
.issue-bar{left:180px;top:0;width:487px;height:24px;background:var(--brown-dark);border-radius:0 6px 0 0;color:var(--white);font-style:italic;font-size:9.5px;display:flex;justify-content:space-between;align-items:center;padding:0 14px}
.card{background:var(--card);border-radius:4px}
.intro{left:214px;top:40px;width:433px;height:143px}
.cert-badge{left:180px;top:55px;width:98px;height:98px;border-radius:50%;background:#cfd9a6;border:5px solid #9cb05a}
.product-shot{left:291px;top:58px;width:62px;height:76px;background:linear-gradient(#f4efe8,#d9cbb8);border-radius:3px}
.intro-title{left:142px;top:10px;font-weight:900;font-style:italic;font-size:19px;color:var(--brown-soft);display:flex;align-items:center;gap:7px;white-space:nowrap}
.intro-title i{display:block;width:22px;height:22px;border-radius:50%;border:3px solid var(--brown-soft)}
.intro-copy{left:170px;top:40px;width:252px;font-style:italic;font-size:8px;line-height:10.5px;color:var(--text-muted);text-align:right}
.intro-copy p+p{margin-top:8px}
.model-photo{left:0;top:140px;width:211px;height:347px;background:linear-gradient(160deg,#e9d2b6,#c98a57 55%,#f1ece4)}
.range{left:214px;top:196px;width:433px;height:291px}
.section-title{font-weight:900;font-size:19px;color:var(--brown)}
.range .section-title{left:11px;top:10px}
.range-item{left:50px;width:370px}
.range-item h3{font-weight:700;font-size:11.5px;color:var(--brown)}
.range-item h3 span{font-weight:400;font-style:italic;font-size:9px;color:var(--grey-caption)}
.range-item p{margin-top:6px;font-style:italic;font-size:8px;line-height:10.5px;color:var(--text-muted)}
.bottle{left:14px;width:20px;border-radius:6px 6px 3px 3px}
.ingredients-band{left:0;top:497px;width:667px;height:35px;background:var(--brown-dark);color:var(--white);font-weight:900;font-size:18px;display:flex;align-items:center;justify-content:center;gap:10px}
.ingredients-band i{display:block;width:8px;height:8px;border-radius:50%;background:var(--white)}
.ingredients-copy{left:40px;top:545px;width:587px;text-align:center;font-style:italic;font-size:8px;line-height:10.5px;color:var(--grey-caption)}
.tile{width:96px;height:96px}
.tile .art{position:absolute;left:10px;top:10px;width:76px;height:76px;border-radius:50%}
.caption{width:110px;text-align:center;font-weight:700;font-size:11px;color:var(--brown);white-space:nowrap}
.caption span{font-weight:400;font-style:italic;font-size:8.5px;color:var(--grey-caption)}
.news-photo{width:111px;height:93px}
.news-copy{font-style:italic;font-size:8px;line-height:10.5px;color:var(--text-muted);text-align:right}
.footer{left:28px;top:1076px;color:var(--white);font-style:italic;font-size:10px;line-height:15px}
</style>
</head>
<body>
<div class="abs proposal-label">DESIGN PROPOSAL FOR</div>
<div class="abs proposal-title">Tidal Quill Is A Premium Spa And Salon Only Professional Tanning Brand</div>

<div class="abs frame">
  <div class="abs panel">
    <div class="abs swoosh-top"></div>
    <div class="abs brand-name"><i></i>Tidal Quill</div>
    <div class="abs issue-bar"><span>Tidal Quill Advertising</span><span>Volume 1 December Issue 2014</span></div>

    <section class="abs card intro">
      <h1 class="abs intro-title"><i></i>A revolution in self tanning</h1>
      <div class="abs intro-copy">
        <p>Tidal Quill has been developed with a unique organic formula, enriched with deep moisturisers and free from paraben and alcohol, ensuring a streak-free, soft finish.</p>
        <p>This organic formula is enriched with deep moisturisers and exotic botanical extracts that tone and firm the skin fighting cellulite whilst developing a naturally youthful, sunkissed glow.</p>
      </div>
    </section>
    <div class="abs cert-badge" role="img" aria-label="Certified organic badge"></div>
    <div class="abs product-shot" role="img" aria-label="Three tanning product bottles"></div>

    <div class="abs model-photo" role="img" aria-label="Woman seen from behind with autumn leaves across her back"></div>

    <section class="abs card range">
      <h2 class="abs section-title">Our Product Range</h2>
      <div class="abs bottle" style="top:44px;height:62px;background:#d9b38c"></div>
      <div class="abs range-item" style="top:44px">
        <h3>Gradual Tan <span>Daily lotion</span></h3>
        <p>Much like our Gradual Tan, our Original and Dark formulas contain an organic formula that comes enriched with the same deep moisturisers and exotic botanicals that help tone and firm the skin, whilst developing a naturally youthful, sun-kissed glow.</p>
      </div>
      <div class="abs bottle" style="top:124px;height:66px;background:#b0643a"></div>
      <div class="abs range-item" style="top:127px">
        <h3>Tanning Mist <span>Original</span></h3>
        <p>This organic formula is enriched with deep moisturisers and exotic botanical extracts that tone and firm the skin fighting cellulite whilst developing a naturally youthful, sunkissed glow.</p>
      </div>
      <div class="abs bottle" style="top:206px;height:70px;background:#7e2c14"></div>
      <div class="abs range-item" style="top:210px">
        <h3>Gradual Tan <span>Dark</span></h3>
        <p>For those with darker skin tones or the preference, these additional products provide the option of a richer deeper colour.</p>
      </div>
    </section>

    <h2 class="abs ingredients-band"><i></i>Our Ingredients<i></i></h2>
    <p class="abs ingredients-copy">Tidal Quill has been developed with a unique organic formula, enriched with deep moisturisers and free from paraben and alcohol, ensuring a streak-free, soft finish. This organic formula is enriched with deep moisturisers and exotic botanical extracts that tone and firm the skin fighting cellulite whilst developing a naturally youthful, sunkissed glow.</p>

    <div class="abs card tile" style="left:24px;top:596px"><div class="art" role="img" aria-label="Chamomile flowers" style="background:radial-gradient(#f4f4ea,#7fa04e)"></div></div>
    <div class="abs card tile" style="left:130px;top:596px"><div class="art" role="img" aria-label="Aloe vera leaves" style="background:radial-gradient(#a8d06a,#4e8a2e)"></div></div>
    <div class="abs card tile" style="left:234px;top:596px"><div class="art" role="img" aria-label="Cocoa butter texture" style="background:radial-gradient(#c99a6a,#8a5a32)"></div></div>
    <div class="abs card tile" style="left:339px;top:596px"><div class="art" role="img" aria-label="Orange" style="background:radial-gradient(#ffae3c,#e7700e)"></div></div>
    <div class="abs card tile" style="left:444px;top:596px"><div class="art" role="img" aria-label="Macadamia nuts" style="background:radial-gradient(#d8b894,#8a5530)"></div></div>
    <div class="abs card tile" style="left:550px;top:596px"><div class="art" role="img" aria-label="Lemon slice" style="background:radial-gradient(#fff2a0,#f2c814)"></div></div>

    <div class="abs caption" style="left:17px;top:705px">Gradual Tan <span>Dark</span></div>
    <div class="abs caption" style="left:123px;top:705px">Gradual Tan <span>Dark</span></div>
    <div class="abs caption" style="left:227px;top:705px">Gradual Tan <span>Dark</span></div>
    <div class="abs caption" style="left:332px;top:705px">Gradual Tan <span>Dark</span></div>
    <div class="abs caption" style="left:437px;top:705px">Gradual Tan <span>Dark</span></div>
    <div class="abs caption" style="left:543px;top:705px">Gradual Tan <span>Dark</span></div>

    <div class="abs card tile" style="left:130px;top:744px"><div class="art" role="img" aria-label="Lime halves" style="background:radial-gradient(#e4f49a,#8cc43a)"></div></div>
    <div class="abs card tile" style="left:234px;top:744px"><div class="art" role="img" aria-label="Spoon of honey" style="background:radial-gradient(#e0a050,#8a3e10)"></div></div>
    <div class="abs card tile" style="left:339px;top:744px"><div class="art" role="img" aria-label="Cinnamon sticks" style="background:radial-gradient(#e6c88a,#a8582a)"></div></div>
    <div class="abs card tile" style="left:444px;top:744px"><div class="art" role="img" aria-label="Grapefruit slice" style="background:radial-gradient(#ffb0a0,#e8503a)"></div></div>

    <div class="abs caption" style="left:123px;top:853px">Gradual Tan <span>Dark</span></div>
    <div class="abs caption" style="left:227px;top:853px">Gradual Tan <span>Dark</span></div>
    <div class="abs caption" style="left:332px;top:853px">Gradual Tan <span>Dark</span></div>
    <div class="abs caption" style="left:437px;top:853px">Gradual Tan <span>Dark</span></div>

    <h2 class="abs section-title" style="left:24px;top:888px">Our News</h2>
    <div class="abs news-photo" style="left:24px;top:920px;background:linear-gradient(135deg,#f2e8da,#c99a6a)" role="img" aria-label="Legs with autumn leaves beside the brand name"></div>
    <p class="abs news-copy" style="left:144px;top:928px;width:186px">Tidal Quill has been developed with a unique organic formula, enriched with deep moisturisers and free from paraben and alcohol, ensuring a streak-free, soft finish.</p>
    <div class="abs news-photo" style="left:346px;top:920px;background:linear-gradient(135deg,#f3d9c4,#d9a07e)" role="img" aria-label="Hands forming a heart over a stomach"></div>
    <p class="abs news-copy" style="left:468px;top:928px;width:180px">Tidal Quill has been developed with a unique organic formula, enriched with deep moisturisers and free from paraben and alcohol, ensuring a streak-free, soft finish.</p>
  </div>
  <div class="abs swoosh-bottom"></div>
  <div class="abs footer">Tidal Quill | hello@tidal-quill-example.com | Kelmoor District Enterprises | Ashfield Road Industrial Estate<br>Kelmoor, County Fenwick KM4 7QD</div>
</div>
</body>
</html>
```